Rivolex.com Trucking Company Website

Need a website designed (no content) for a trucking company, specializing in trucking of ocean containers (intermodal Trucking). Heavy emphasis on technology, using latest technology, providing unabated visibility and realtime information.
clean minimalist industrial website
example:
https://www.bramtiq.com/

Target Market(s)

Professional Business Consumer corporate and small business

Industry/Entity Type

Trucking Company

Number of Pages Required

5+ page

Requirements
Must have
• Industrial Design, simple informative, for a busy professional to view and get the necessary information with out the distractions.
• Blog Page
• Client Log-In on the front page
• Technology page - showing our intensive investments in technology
Nice to have
• If ANY images included, MUST be USA related. Example if include an image of a truck, ensure its a USA model. Do the research.
• included our business card for sample of Logo
• Doesnt not have to be the same color schemes.
Should not have
• moving images

```html
<!DOCTYPE html>
<html lang="en">
<head>
<meta charset="utf-8">
<title>Rivolex Consulting</title>
<link rel="stylesheet" href="https://fonts.googleapis.com/css2?family=Roboto:wght@300;400;500;700&display=swap">
<style>
  :root {
    --white: #ffffff;
    --ink: #1d1f24;
    --muted: #6b7079;
    --brand-blue: #0f4c9c;
    --dot-blue: #4d86c9;
    --soft-bg: #f3f4f6;
    --rule: #e3e5e9;
    --hero-top: #74879b;
    --hero-bottom: #7e8086;
    --page-bg: #ffffff;
  }
  * { box-sizing: border-box; margin: 0; padding: 0; }
  html, body { width: 1200px; height: 676px; overflow: hidden; background: var(--page-bg); }
  body { font-family: "Roboto", Arial, sans-serif; color: var(--ink); position: relative; }

  .hero { position: relative; width: 1200px; height: 496px; overflow: hidden; }
  .hero-photo {
    position: absolute; inset: 0;
    background: linear-gradient(180deg, var(--hero-top) 0%, var(--hero-bottom) 100%);
  }
  .hero-sheen { position: absolute; inset: 0; }

  .site-nav {
    position: absolute; top: 0; left: 0; right: 0; height: 68px;
    display: flex; align-items: center; padding: 0 30px;
    border-bottom: 1px solid rgba(255,255,255,0.35);
  }
  .brand { display: flex; align-items: center; gap: 8px; color: var(--white); font-weight: 700; font-size: 26px; letter-spacing: 2px; width: 270px; }
  .brand-mark { width: 12px; height: 12px; background: var(--white); }
  .menu { display: flex; gap: 34px; list-style: none; margin-left: 20px; }
  .menu li { color: var(--white); font-size: 14px; font-weight: 500; letter-spacing: 0.3px; }
  .account { margin-left: auto; display: flex; gap: 8px; }
  .btn { font-size: 12px; font-weight: 500; padding: 6px 12px; border-radius: 16px; border: 1.5px solid var(--white); }
  .btn-login { color: var(--white); }
  .btn-quote { background: var(--white); color: var(--ink); }

  .hero-title {
    position: absolute; left: 150px; top: 170px; width: 240px;
    text-align: center; color: var(--white); font-weight: 400; font-size: 26px; line-height: 31px; letter-spacing: 1px;
  }
  .hero-title strong { display: block; font-size: 38px; line-height: 40px; font-weight: 700; }

  .info-bar {
    height: 34px; display: flex; align-items: center; padding: 0 60px;
    border-bottom: 1px solid var(--rule); font-size: 12px; color: var(--muted);
  }
  .info-item { display: flex; align-items: center; gap: 6px; margin-right: 26px; }
  .info-social { margin-left: auto; display: flex; gap: 12px; align-items: center; }
  .social-dot { width: 16px; height: 16px; border-radius: 3px; background: var(--dot-blue); }

  .welcome { text-align: center; padding-top: 8px; }
  .section-title { font-size: 20px; font-weight: 500; color: var(--ink); }
  .section-title span { color: var(--brand-blue); }
  .welcome-rule { margin: 10px 50px 0; border-top: 2px dotted var(--dot-blue); }
  .welcome-text { font-size: 12px; line-height: 18px; color: var(--ink); margin: 12px 60px 0; }

  .technology { position: absolute; left: 0; right: 0; top: 634px; bottom: 0; background: var(--soft-bg); text-align: center; padding-top: 10px; }
</style>
</head>
<body>
  <header class="hero">
    <div class="hero-photo" role="img" aria-label="Photo of a grey semi truck hauling heavy equipment along a highway"></div>
    <svg class="hero-sheen" width="1200" height="496" aria-hidden="true">
      <polygon points="560,68 1200,68 1200,496 380,496" fill="rgba(255,255,255,0.08)"/>
    </svg>
    <nav class="site-nav">
      <div class="brand"><span class="brand-mark"></span>RIVOLEX</div>
      <ul class="menu">
        <li>HOME</li><li>ABOUT US</li><li>TECHNOLOGY</li><li>BLOG</li><li>CONTACT</li>
      </ul>
      <div class="account">
        <span class="btn btn-login">Log In</span>
        <span class="btn btn-quote">Request a Quote</span>
      </div>
    </nav>
    <h1 class="hero-title">THE REAL <strong>KING</strong> OF<br>INVESTMENTS<br>IN TECHNOLOGY</h1>
  </header>

  <div class="info-bar">
    <span class="info-item">
      <svg width="12" height="12" viewBox="0 0 24 24" aria-hidden="true"><path fill="#6b7079" d="M6.6 10.8a15 15 0 0 0 6.6 6.6l2.2-2.2a1 1 0 0 1 1-.25 11.4 11.4 0 0 0 3.6.6 1 1 0 0 1 1 1V20a1 1 0 0 1-1 1A17 17 0 0 1 3 4a1 1 0 0 1 1-1h3.5a1 1 0 0 1 1 1c0 1.25.2 2.45.6 3.6a1 1 0 0 1-.25 1z"/></svg>
      +1 555 014 27 38
    </span>
    <span class="info-item">
      <svg width="13" height="10" viewBox="0 0 26 20" aria-hidden="true"><rect x="1" y="1" width="24" height="18" fill="#6b7079"/><path d="M1 1l12 10L25 1" stroke="#fff" stroke-width="2" fill="none"/></svg>
      info@rivolex.com
    </span>
    <div class="info-social">
      <span class="social-dot" aria-label="Social profile"></span>
      <span class="social-dot" aria-label="Social profile"></span>
      <svg width="13" height="13" viewBox="0 0 24 24" aria-label="Search"><circle cx="10" cy="10" r="6" stroke="#6b7079" stroke-width="3" fill="none"/><line x1="15" y1="15" x2="21" y2="21" stroke="#6b7079" stroke-width="3"/></svg>
    </div>
  </div>

  <section class="welcome">
    <h2 class="section-title">Welcome to <span>Rivolex Consulting</span></h2>
    <div class="welcome-rule"></div>
    <p class="welcome-text">Sed ut perspiciatis unde omnis iste natus error sit voluptatem accusantium doloremque laudantium, totam rem aperiam, eaque ipsa quae ab illo inventore veritatis et quasi architecto beatae vitae dicta sunt explicabo.</p>
  </section>

  <section class="technology">
    <h2 class="section-title">Our <span>Technology</span></h2>
  </section>
</body>
</html>
```